Brochure Design Project

This will be a tri-fold full 8.5x11 brochure that will be distributed and sitting in Oncology offices all throughout the US. It is a lead generation and referral designed piece that it to target all patients, Cancer primarily, but all critically ill patients and seniors above the age of 70. We want our service to go beyond just a financial transaction, we want to educate patients of their rights within a life insurance policy and if we cannot help them personally, do want to assist them by referring them to other agencies and non profits than can. ( I want to redesign the brochure attached, it can be very similar and need only minor changes to content, but would welcome all suggestions on improving message, and in gaining attention, picture substitutions and change of colors, along with the layout itself can be improved upon, and I need this piece to look very professional and appropriate for medical offices. I will be needing assistance on several upcoming projects and will also have great printing demands.

Target Market(s)

Cancer patients
all chronically and critically ill patients
all seniors above age 70

Industry/Entity Type

Life Insurance

Requirements
Must have
• Cancer and the terminally ill
Nice to have
• seniors above 70

```html
<!DOCTYPE html>
<html lang="en">
<head>
<meta charset="utf-8">
<title>Brightway Settlements — Tri-fold Brochure</title>
<link rel="stylesheet" href="https://fonts.googleapis.com/css2?family=Roboto+Condensed:wght@400;700&family=Roboto:wght@400;700&display=swap">
<style>
:root{
  --blue:#1b7cc6;
  --blue-deep:#0c4f93;
  --blue-mid:#2a8fd6;
  --blue-pale:#d3ebfa;
  --blue-mist:#eaf6fd;
  --gold:#f6c01e;
  --gold-deep:#e49b0f;
  --ink:#0b2a4a;
  --white:#ffffff;
  --stage:#ece9e4;
  --head:'Roboto Condensed',Arial,sans-serif;
  --body:'Roboto',Arial,sans-serif;
}
*{box-sizing:border-box;margin:0;padding:0}
html,body{width:1200px;height:1080px;overflow:hidden;background:var(--stage);font-family:var(--body);color:var(--white)}
.spread{position:absolute;left:270px;width:660px;height:510px;display:flex;box-shadow:0 6px 18px rgba(0,0,0,.25)}
.spread--outside{top:20px}
.spread--inside{top:550px}
.panel{position:relative;width:220px;height:510px;overflow:hidden;background:linear-gradient(180deg,var(--blue-mid),var(--blue-deep))}
.panel + .panel{border-left:1px solid rgba(255,255,255,.35)}
.photo{position:absolute;left:0;width:100%}
.web{position:absolute;bottom:8px;left:0;width:100%;text-align:center;font-size:8px;color:var(--white);opacity:.85}
.badge{background:linear-gradient(180deg,#ffd84a,var(--gold-deep));color:var(--ink);font-family:var(--head);font-weight:700;text-align:center;border-radius:6px;border:2px solid var(--white);text-transform:uppercase;line-height:1.1}
.brand{display:flex;align-items:center;justify-content:center;gap:6px;font-family:var(--head);font-weight:700;color:var(--blue-deep);letter-spacing:1px}
.brand-dot{width:12px;height:12px;border-radius:50%;background:var(--gold)}

/* outside: benefits panel */
.benefits .photo{top:0;height:128px;background:linear-gradient(135deg,#f2f6f8,#a9c6dc 60%,#3b7fb8)}
.benefits-title{position:absolute;top:136px;left:14px;font-family:var(--head);font-weight:700;font-size:15px}
.checklist{position:absolute;top:160px;left:14px;right:10px;list-style:none;font-size:8.4px;line-height:1.42}
.checklist li{display:flex;gap:4px;align-items:center}
.checklist svg{flex:none}
.benefits .badge{position:absolute;left:22px;right:22px;top:432px;padding:6px 4px;font-size:12px}

/* outside: reply panel */
.reply{background:linear-gradient(180deg,var(--blue-mist),var(--blue-pale))}
.reply-card{position:absolute;width:510px;height:220px;left:-145px;top:145px;transform:rotate(90deg);display:flex;color:var(--blue-deep)}
.reply-mail{width:270px;padding:16px 14px;position:relative}
.reply-mail h3{font-family:var(--head);font-size:17px;font-weight:700}
.reply-mail .fine{font-size:7px;line-height:1.4;margin-top:2px;color:var(--ink)}
.reply-mail .to{margin-top:44px;font-family:var(--head);font-size:13px;line-height:1.3;color:var(--ink)}
.reply-mail .to strong{color:var(--blue);font-size:15px}
.postage{position:absolute;right:10px;top:12px;width:50px;height:40px;border:1px solid var(--ink);font-size:5.5px;text-align:center;padding:4px;color:var(--ink)}
.reply-logo{flex:1;margin:12px;border:2px solid var(--blue);border-radius:6px;background:var(--white);display:flex;flex-direction:column;align-items:center;justify-content:center;gap:6px;text-align:center}
.reply-logo .brand{font-size:17px}
.reply-logo p{font-size:9px;color:var(--blue-deep);font-weight:700;line-height:1.3}
.phone-line{display:flex;align-items:center;gap:5px;font-family:var(--head);font-weight:700}
.reply-logo .phone-line{font-size:19px;color:var(--blue-deep)}
.reply-logo .fine{font-size:7px;font-weight:400}

/* outside: cover */
.cover-top{position:absolute;top:0;left:0;right:0;height:92px;background:linear-gradient(180deg,var(--white),var(--blue-pale));display:flex;align-items:center;justify-content:center}
.cover-top .brand{font-size:22px}
.cover .photo{top:92px;height:206px;background:linear-gradient(160deg,#4f7d3c,#8fa97d 45%,#c9b8a8 70%,#7a8a98)}
.cover-copy{position:absolute;top:298px;left:0;right:0;bottom:0;text-align:center}
.headline{font-family:var(--head);font-weight:700;font-size:23px;line-height:1.05;padding:14px 6px 6px;text-transform:uppercase;text-shadow:0 1px 2px rgba(0,0,0,.35)}
.subline{font-family:var(--head);font-weight:700;color:var(--gold);font-size:13px;line-height:1.25}
.cover-phone{margin:10px 14px 0;background:var(--blue-pale);color:var(--blue-deep);justify-content:center;font-size:17px;padding:3px;border-radius:2px}
.waiting{font-family:var(--head);font-size:15px;margin-top:8px}

/* inside: money panel */
.money-tab{position:absolute;top:8px;left:0;right:0;text-align:center;font-family:var(--head);font-weight:700;font-size:13px;background:var(--blue-deep);padding:2px}
.framed{position:absolute;background:var(--white);padding:6px;box-shadow:0 3px 8px rgba(0,0,0,.3)}
.framed div{width:100%;height:100%}
.money .framed{top:34px;left:16px;width:188px;height:140px}
.money .framed div{background:linear-gradient(135deg,#f0e2d0,#c7a58a 55%,#7fa9c6)}
.why{position:absolute;top:190px;left:14px;right:12px;font-size:9.4px;line-height:1.32}
.why p{margin-bottom:7px}
.why b{color:var(--gold);font-family:var(--head);font-size:11px}
.money .badge{position:absolute;left:16px;right:16px;top:432px;padding:5px 4px;font-size:10px}

/* inside: journey panel */
.journey-intro{position:absolute;top:14px;left:14px;right:12px;font-size:9.4px;line-height:1.35}
.journey-intro b{color:var(--gold)}
.turning{position:absolute;top:116px;left:0;right:0;text-align:center;font-family:var(--head);font-weight:700;font-size:20px;line-height:1.05;color:var(--gold);text-transform:uppercase}
.journey .badge{position:absolute;top:170px;left:24px;right:24px;padding:4px}
.journey .badge strong{display:block;font-size:20px}
.journey .badge span{display:block;font-size:9px;text-transform:none}
.journey .framed{top:250px;left:30px;width:160px;height:148px}
.journey .framed div{background:linear-gradient(160deg,#e8eef2,#b9c7d2 55%,#6b5548)}

/* inside: enquiry panel */
.enquiry{background:linear-gradient(180deg,var(--blue-mid) 0%,var(--blue-deep) 48%,var(--blue-pale) 48%,var(--blue-mist) 100%)}
.enquiry-top{position:absolute;top:12px;left:12px;right:12px;font-size:8.6px;line-height:1.35}
.eligible{margin-top:8px;font-family:var(--head);font-weight:700;font-size:11px;text-transform:uppercase}
.eligible strong{display:block;color:var(--gold);font-size:18px}
.enquiry-top .call{margin-top:6px;font-size:10px;text-align:center;line-height:1.35}
.enquiry-top .phone-line{justify-content:center;font-size:20px;margin-top:6px}
.form{position:absolute;top:262px;left:12px;right:12px;color:var(--blue-deep)}
.form h4{font-family:var(--head);font-size:11px;text-transform:uppercase;margin-bottom:6px}
.form-row{display:flex;align-items:flex-end;gap:4px;height:21px;font-size:8px;border-bottom:1px solid var(--blue)}
.form .fine{margin-top:8px;font-size:7px;color:var(--ink)}
.enquiry .web{color:var(--blue-deep)}
</style>
</head>
<body>

<!-- Outside spread -->
<section class="spread spread--outside">
  <article class="panel benefits">
    <div class="photo" role="img" aria-label="Photo of a nurse caring for a smiling senior patient"></div>
    <h2 class="benefits-title">Brightway Settlements</h2>
    <ul class="checklist">
      <li><svg width="8" height="8" viewBox="0 0 8 8"><path d="M1 4l2 2 4-5" stroke="#f6c01e" stroke-width="1.5" fill="none"/></svg>Reduce Financial Stress</li>
      <li><svg width="8" height="8" viewBox="0 0 8 8"><path d="M1 4l2 2 4-5" stroke="#f6c01e" stroke-width="1.5" fill="none"/></svg>Pay for Uninsured Healthcare Cost</li>
      <li><svg width="8" height="8" viewBox="0 0 8 8"><path d="M1 4l2 2 4-5" stroke="#f6c01e" stroke-width="1.5" fill="none"/></svg>Pay for Alternative Treatment</li>
      <li><svg width="8" height="8" viewBox="0 0 8 8"><path d="M1 4l2 2 4-5" stroke="#f6c01e" stroke-width="1.5" fill="none"/></svg>Improve Quality of Life</li>
      <li><svg width="8" height="8" viewBox="0 0 8 8"><path d="M1 4l2 2 4-5" stroke="#f6c01e" stroke-width="1.5" fill="none"/></svg>Pay off Debt</li>
      <li><svg width="8" height="8" viewBox="0 0 8 8"><path d="M1 4l2 2 4-5" stroke="#f6c01e" stroke-width="1.5" fill="none"/></svg>Take a Long Awaited Vacation or Dream Trip</li>
      <li><svg width="8" height="8" viewBox="0 0 8 8"><path d="M1 4l2 2 4-5" stroke="#f6c01e" stroke-width="1.5" fill="none"/></svg>Make Cash Gifts to Family and Friends</li>
      <li><svg width="8" height="8" viewBox="0 0 8 8"><path d="M1 4l2 2 4-5" stroke="#f6c01e" stroke-width="1.5" fill="none"/></svg>Fulfill Life Wishes</li>
      <li><svg width="8" height="8" viewBox="0 0 8 8"><path d="M1 4l2 2 4-5" stroke="#f6c01e" stroke-width="1.5" fill="none"/></svg>Pay for College Funding</li>
      <li><svg width="8" height="8" viewBox="0 0 8 8"><path d="M1 4l2 2 4-5" stroke="#f6c01e" stroke-width="1.5" fill="none"/></svg>Make Home Improvements</li>
      <li><svg width="8" height="8" viewBox="0 0 8 8"><path d="M1 4l2 2 4-5" stroke="#f6c01e" stroke-width="1.5" fill="none"/></svg>Donate to Church or Charity</li>
      <li><svg width="8" height="8" viewBox="0 0 8 8"><path d="M1 4l2 2 4-5" stroke="#f6c01e" stroke-width="1.5" fill="none"/></svg>See the Money Enjoyed by Relatives Now</li>
      <li><svg width="8" height="8" viewBox="0 0 8 8"><path d="M1 4l2 2 4-5" stroke="#f6c01e" stroke-width="1.5" fill="none"/></svg>Invest in Financial Vehicles</li>
      <li><svg width="8" height="8" viewBox="0 0 8 8"><path d="M1 4l2 2 4-5" stroke="#f6c01e" stroke-width="1.5" fill="none"/></svg>Buy a New Car</li>
      <li><svg width="8" height="8" viewBox="0 0 8 8"><path d="M1 4l2 2 4-5" stroke="#f6c01e" stroke-width="1.5" fill="none"/></svg>Fund Long Term Care Expenses</li>
      <li><svg width="8" height="8" viewBox="0 0 8 8"><path d="M1 4l2 2 4-5" stroke="#f6c01e" stroke-width="1.5" fill="none"/></svg>Plan Ahead for Final Estate Needs</li>
    </ul>
    <div class="badge">Hope is our desired<br>gift to you!</div>
    <div class="web">www.brightwaysettlements.com</div>
  </article>

  <article class="panel reply">
    <div class="reply-card">
      <div class="reply-mail">
        <h3>BUSINESS REPLY MAIL</h3>
        <p class="fine">FIRST-CLASS MAIL &nbsp; PERMIT NO. 0000 &nbsp; MAPLE GROVE GA<br>POSTAGE WILL BE PAID BY ADDRESSEE</p>
        <div class="postage">NO POSTAGE NECESSARY IF MAILED IN THE UNITED STATES</div>
        <p class="to"><strong>BRIGHTWAY SETTLEMENTS</strong><br>418 Willow Creek Dr, Maple Grove,<br>Georgia 30099</p>
      </div>
      <div class="reply-logo">
        <div class="brand"><span class="brand-dot"></span>BRIGHTWAY SETTLEMENTS</div>
        <p>Please return the attached postcard or<br>Call Toll Free</p>
        <div class="phone-line"><svg width="16" height="16" viewBox="0 0 16 16"><circle cx="8" cy="8" r="8" fill="#0c4f93"/><path d="M5 4c1 0 1.5 2 1 2.5l-.6.6c.5 1.2 1.3 2 2.5 2.5l.6-.6c.5-.5 2.5 0 2.5 1 0 .8-1 1.5-1.8 1.5C6.5 11.5 4.5 9.5 4.5 6.3 4.5 5 4.3 4 5 4z" fill="#fff"/></svg>800-555-0147</div>
        <p class="fine">All communication will be kept strictly confidential</p>
      </div>
    </div>
  </article>

  <article class="panel cover">
    <div class="cover-top"><div class="brand"><span class="brand-dot"></span>BRIGHTWAY</div></div>
    <div class="photo" role="img" aria-label="Photo of a woman undergoing cancer treatment, looking ahead calmly outdoors"></div>
    <div class="cover-copy">
      <h1 class="headline">Discover<br>Financial Freedom</h1>
      <p class="subline">Your Not Alone<br>Financial Resources are Available</p>
      <div class="phone-line cover-phone"><svg width="16" height="16" viewBox="0 0 16 16"><circle cx="8" cy="8" r="8" fill="#0c4f93"/><path d="M5 4c1 0 1.5 2 1 2.5l-.6.6c.5 1.2 1.3 2 2.5 2.5l.6-.6c.5-.5 2.5 0 2.5 1 0 .8-1 1.5-1.8 1.5C6.5 11.5 4.5 9.5 4.5 6.3 4.5 5 4.3 4 5 4z" fill="#fff"/></svg>800-555-0147</div>
      <p class="waiting">We are Waiting to Help!</p>
    </div>
    <div class="web">www.brightwaysettlements.com</div>
  </article>
</section>

<!-- Inside spread -->
<section class="spread spread--inside">
  <article class="panel money">
    <div class="money-tab">It's Your Money</div>
    <div class="framed"><div role="img" aria-label="Photo of a smiling senior couple"></div></div>
    <div class="why">
      <p><b>Why</b> do insurance companies conceal the fact that policy holders may be entitled to additional cash benefits?</p>
      <p><b>Why</b> are bankruptcy rates among cancer patients and seniors more than double than that of the general population?</p>
      <p><b>Why</b> do patients who are receiving care feel unsure about discussing the subject of money and effects it can have both emotionally and physically?</p>
    </div>
    <div class="badge">Healing &amp; recovery should be the primary concern for all patients "not money" or "the lack of"</div>
    <div class="web">www.brightwaysettlements.com</div>
  </article>

  <article class="panel journey">
    <p class="journey-intro"><b>Everyone</b> on the journey of medical recovery should have access to FINANCIAL SUPPORT that improves quality of life and provides relief from distress.<br><b>We can Help</b> provide the information and guidance you need to learn more about your FINANCIAL RESOURCES AVAILABLE</p>
    <h2 class="turning">Turning "Hope"<br>into Reality</h2>
    <div class="badge"><strong>800-555-0147</strong><span>www.brightwaysettlements.com</span></div>
    <div class="framed"><div role="img" aria-label="Photo of a smiling senior man resting in a hospital bed"></div></div>
    <div class="web">www.brightwaysettlements.com</div>
  </article>

  <article class="panel enquiry">
    <div class="enquiry-top">
      <p>Have you been diagnosed with a life threatening illness and own life insurance or covered by a group policy?</p>
      <p>Were you born before 1945 and own life insurance or covered by a group policy?</p>
      <p class="eligible">You may be eligible to receive a <strong>Settlement</strong></p>
      <p class="call">Call Today to Receive your Free &amp; Confidential Settlement Kit or Ask one of our Family Service Counselors for Assistance or Advise on Where to Turn</p>
      <div class="phone-line"><svg width="18" height="18" viewBox="0 0 16 16"><circle cx="8" cy="8" r="8" fill="#fff"/><path d="M5 4c1 0 1.5 2 1 2.5l-.6.6c.5 1.2 1.3 2 2.5 2.5l.6-.6c.5-.5 2.5 0 2.5 1 0 .8-1 1.5-1.8 1.5C6.5 11.5 4.5 9.5 4.5 6.3 4.5 5 4.3 4 5 4z" fill="#0c4f93"/></svg>800-555-0147</div>
    </div>
    <div class="form">
      <h4>Please send me a free information kit</h4>
      <div class="form-row">Name:</div>
      <div class="form-row">Address:</div>
      <div class="form-row">City: &nbsp;&nbsp;&nbsp;&nbsp;&nbsp;&nbsp;&nbsp;&nbsp;&nbsp;&nbsp;&nbsp;&nbsp;&nbsp;&nbsp;&nbsp; State: &nbsp;&nbsp;&nbsp;&nbsp;&nbsp;&nbsp;&nbsp; Zip:</div>
      <div class="form-row">Email Address:</div>
      <div class="form-row">Phone: &nbsp;&nbsp;&nbsp;&nbsp;&nbsp;&nbsp;&nbsp;&nbsp;&nbsp;&nbsp;&nbsp;&nbsp;&nbsp;&nbsp;&nbsp;&nbsp;&nbsp; AM / PM</div>
      <div class="form-row">Best time to call:</div>
      <div class="form-row">Insurance Co:</div>
      <p class="fine">All communication will be kept strictly confidential</p>
    </div>
    <div class="web">www.brightwaysettlements.com</div>
  </article>
</section>

</body>
</html>
```